INNOVATIVE DESIGN NEEDED FOR FINANCIAL COMPANY

INTERNATIONAL FIRM IN HONG KONG NEEDS A MODERN BUSINESS CARD DESIGN. ONE SIDE ENGLISH OTHER SIDE IN CHINESE. WE ARE OPEN TO CHANGING FONTS AND COLOR. SHOULD BE A CARD THAT IS PROFESSIONAL DEALING WITH HIGH NET WORTH CLIENTELE. BOTH SIDES OF THE CARD WILL BE THE SAME, HOWEVER, THE WORDING ON ONE SIDE WILL BE ENGLISH AND THE OTHER SIDE IN CHINESE (CAN ASSIST IN THE LETTERING - CAN PROVIDE ONCE CARD DESIGN IS ACCEPTED.

Target Market(s)

Hong Kong/CHINA

Contact Information for Business Card

ATTRACTIVE MODERN

```html
<!DOCTYPE html>
<html lang="en">
<head>
<meta charset="utf-8">
<title>Larchwood Asset Management – Business Card</title>
<link rel="stylesheet" href="https://fonts.googleapis.com/css2?family=Arimo:wght@400;700&family=Noto+Sans+TC:wght@900&display=swap">
<style>
  :root {
    --brand-green: #0b7a55;
    --ink: #2b2b2b;
    --rule: #6a6a6a;
    --card: #f4f4f3;
    --backdrop: #cfcfd0;
  }
  * { margin: 0; padding: 0; box-sizing: border-box; }
  html, body {
    width: 1200px; height: 1000px; overflow: hidden;
    background: var(--backdrop);
    font-family: "Arimo", Arial, sans-serif;
  }
  .card {
    position: absolute; left: 60px; top: 198px;
    width: 1080px; height: 603px;
    background: var(--card);
    color: var(--ink);
  }
  .card__band {
    position: absolute; left: 0; top: 0; width: 100%; height: 23px;
    background: var(--brand-green);
  }
  .wordmark { position: absolute; left: 75px; top: 118px; color: var(--ink); }
  .wordmark__zh {
    font-family: "Noto Sans TC", sans-serif; font-weight: 900;
    font-size: 35px; letter-spacing: 3px; line-height: 1;
  }
  .wordmark__en {
    font-family: "Arimo", Arial, sans-serif; font-weight: 700;
    font-size: 19px; letter-spacing: 3.1px; line-height: 1; margin-top: 4px;
  }
  .brand-mark { position: absolute; left: 764px; top: 99px; width: 238px; text-align: center; }
  .brand-mark__circle {
    width: 238px; height: 238px; border-radius: 50%;
    background: var(--brand-green);
  }
  .person { position: absolute; left: 74px; top: 340px; }
  .person__name {
    color: var(--brand-green); font-weight: 700; font-size: 34px; line-height: 1;
  }
  .person__title { font-size: 24px; margin-top: 6px; }
  .divider {
    position: absolute; left: 75px; top: 464px; width: 930px; height: 2px;
    background: var(--rule);
  }
  .contact {
    position: absolute; left: 75px; top: 478px; width: 930px;
    font-size: 24px; line-height: 31px;
  }
  .contact__line { display: flex; justify-content: space-between; white-space: nowrap; }
  .contact__label { color: var(--brand-green); font-weight: 700; margin-right: 14px; }
  .contact__sep { margin: 0 4px; }
</style>
</head>
<body>
  <div class="card">
    <div class="card__band"></div>

    <div class="wordmark">
      <div class="wordmark__zh">林樺資產管理有限公司</div>
      <div class="wordmark__en">Larchwood Asset Management Ltd</div>
    </div>

    <div class="brand-mark">
      <div class="brand-mark__circle"></div>
    </div>

    <div class="person">
      <div class="person__name">MORGAN WHITFIELD</div>
      <div class="person__title">General Manager</div>
    </div>

    <div class="divider"></div>

    <div class="contact">
      <div class="contact__line">Suite 12 Floor 9 Harbourline Tower, 88 Canal View Rd Kwun Tong KLN</div>
      <div class="contact__line">
        <span><span class="contact__label">Tel:</span>(852) 2700-0148</span>
        <span class="contact__sep">·</span>
        <span><span class="contact__label">Email:</span>info@larchwoodasset.com</span>
        <span class="contact__sep">·</span>
        <span>www.larchwoodasset.com</span>
      </div>
    </div>
  </div>
</body>
</html>
```